Power Point Template for Company

I would like a power point template for my company. This will be the template that we use for all presentations. I have attached our company logo and would like it incorporated into the template. Thanks.

```html
<!DOCTYPE html>
<html lang="en">
<head>
<meta charset="utf-8">
<title>Vulpo Design – Presentation Template</title>
<link href="https://fonts.googleapis.com/css2?family=Audiowide&family=Montserrat:wght@400;500;600&display=swap" rel="stylesheet">
<style>
:root{
  --orange:#f47a1f;
  --orange-deep:#e8670f;
  --ink:#1b1b1b;
  --text:#3a3a3a;
  --muted:#5d5d5d;
  --paper:#f4f4f4;
  --canvas:#e9e9e9;
  --panel:#5f5a57;
  --white:#ffffff;
}
*{box-sizing:border-box;margin:0;padding:0}
html,body{width:1200px;height:3945px;overflow:hidden;background:var(--canvas)}
body{position:relative;font-family:"Montserrat",sans-serif;color:var(--text)}
.slide{position:absolute;left:52px;width:1096px;height:617px;overflow:hidden;
  background:repeating-radial-gradient(circle at 30% 45%,#f6f6f6 0 60px,#efefef 60px 62px,#f6f6f6 62px 120px);
  box-shadow:0 1px 3px rgba(0,0,0,.12)}
.abs{position:absolute}
.display{font-family:"Audiowide",sans-serif;font-weight:400}
.brand{position:absolute;display:flex;align-items:center;gap:10px}
.brand-dot{width:56px;height:56px;border-radius:50%;background:var(--orange)}
.brand-name{font-family:"Montserrat",sans-serif;font-weight:600;font-size:26px;letter-spacing:2px;color:var(--ink);line-height:1}
.brand-name small{display:block;font-size:11px;letter-spacing:7px;color:var(--ink);margin-top:6px}
.brand.light .brand-dot{background:var(--white)}
.brand.light .brand-name,.brand.light .brand-name small{color:var(--white)}
.banner-left{position:absolute;background:var(--orange);border-radius:0 60px 60px 0;color:var(--white)}
.banner-right{position:absolute;background:var(--orange);border-radius:60px 0 0 60px;color:var(--white);
  font-family:"Audiowide",sans-serif;font-size:44px;padding-left:48px;display:flex;align-items:center}
.copy{font-size:13.5px;line-height:26px;color:var(--text);text-align:justify}
.photo{position:absolute;border-radius:2px}

/* slide 1 */
.welcome{left:73px;top:218px;font-size:24px;color:var(--ink)}
.hero-band{left:0;top:265px;width:511px;height:86px;font-size:56px;padding-left:50px;display:flex;align-items:center}
.hero-sub{left:56px;top:368px;font-size:40px;color:var(--orange)}
.phone{left:56px;top:466px;display:flex;align-items:center;gap:14px;font-size:12px;font-weight:600;color:var(--ink)}

/* slide 2 */
.h-sub{font-family:"Montserrat",sans-serif;font-weight:500;font-size:28px;color:var(--ink);display:flex;align-items:center;gap:10px}

/* slide 3 */
.services-top{left:0;top:0;width:1096px;height:395px;background:linear-gradient(180deg,#f07a22,#f0781c)}
.services-top::after{content:"";position:absolute;inset:0;background:linear-gradient(90deg,rgba(120,50,10,.0),rgba(120,50,10,.12) 40%,rgba(120,50,10,.08))}
.white-band{left:0;top:130px;width:510px;height:86px;background:var(--white);border-radius:0 60px 60px 0;
  font-family:"Audiowide",sans-serif;font-size:40px;color:var(--ink);padding-left:80px;display:flex;align-items:center}
.services-copy{left:617px;top:58px;width:450px;font-size:14px;line-height:31.5px;color:var(--white)}
.service{position:absolute;top:303px;width:250px;text-align:center}
.service-ring{width:184px;height:184px;border-radius:50%;background:var(--white);margin:0 auto;position:relative}
.service-dot{position:absolute;left:12px;top:12px;width:160px;height:160px;border-radius:50%;display:flex;align-items:center;justify-content:center}
.service-dot.orange{background:var(--orange)}
.service-dot.black{background:var(--ink)}
.service h3{font-weight:500;font-size:20px;color:var(--ink);margin-top:14px}
.service p{font-size:10.5px;line-height:17px;color:var(--muted);margin-top:8px}

/* slide 5 */
.stat{position:absolute;width:184px;height:184px;border-radius:50%;background:var(--white)}
.stat-core{position:absolute;left:6px;top:12px;width:168px;height:168px;border-radius:50%;
  display:flex;align-items:center;justify-content:center;text-align:center;color:var(--white);font-weight:500;font-size:20px;line-height:27px}
.stat-core.orange{background:var(--orange)}
.stat-core.black{background:var(--ink)}

/* slide 6 */
.member{position:absolute;top:192px;width:250px;text-align:center}
.member .portrait{width:178px;height:178px;border-radius:50%;margin:0 auto;background:radial-gradient(circle at 50% 40%,#6a6f78,#2c3038)}
.member h4{font-weight:500;font-size:16px;color:var(--ink);margin-top:36px;text-transform:uppercase;letter-spacing:.3px}
.member p{font-size:10px;line-height:18px;color:var(--muted);margin-top:12px}
</style>
</head>
<body>

<!-- Title -->
<section class="slide" style="top:46px">
  <div class="brand" style="left:70px;top:84px"><span class="brand-dot"></span><span class="brand-name">VULPO<small>DESIGN</small></span></div>
  <div class="abs display welcome">Welcome To</div>
  <div class="banner-left display hero-band">VULPO</div>
  <div class="abs display hero-sub">DESIGN</div>
  <div class="abs phone">
    <svg width="34" height="34" viewBox="0 0 34 34"><circle cx="17" cy="17" r="15.5" fill="none" stroke="#1b1b1b" stroke-width="1.5"/><path d="M12 10c1-1 2-1 2.6 0l1.6 2.6c.4.7.2 1.4-.4 1.9l-1 .8c.8 1.8 2.2 3.2 4 4l.8-1c.5-.6 1.2-.8 1.9-.4l2.6 1.6c1 .6 1 1.6 0 2.6-1.4 1.4-3.4 1.6-5.4.6-3.2-1.6-5.6-4-7.2-7.2-1-2-.8-4 .5-5.5z" fill="none" stroke="#1b1b1b" stroke-width="1.4"/></svg>
    +1 555 014 2290
  </div>
  <svg class="abs" style="left:560px;top:40px" width="540" height="540" viewBox="0 0 540 540">
    <circle cx="272" cy="258" r="256" fill="var(--orange)"/>
    <circle cx="253" cy="275" r="232" fill="#f6f6f6"/>
    <circle cx="246" cy="277" r="218" fill="url(#night)" role="img" aria-label="Night city street with large illuminated advertising screens"/>
    <defs><radialGradient id="night" cx="50%" cy="45%" r="60%"><stop offset="0" stop-color="#5a6fc0"/><stop offset=".5" stop-color="#26285a"/><stop offset="1" stop-color="#0b0b1a"/></radialGradient></defs>
  </svg>
</section>

<!-- About -->
<section class="slide" style="top:696px">
  <div class="brand" style="left:46px;top:35px"><span class="brand-dot"></span><span class="brand-name">VULPO<small>DESIGN</small></span></div>
  <div class="banner-right" style="left:553px;top:28px;width:543px;height:84px">ABOUT US</div>
  <svg class="abs" style="left:0;top:140px" width="520" height="477" viewBox="0 0 520 477">
    <defs><linearGradient id="neon" x1="0" y1="0" x2="1" y2="1"><stop offset="0" stop-color="#2b1d5c"/><stop offset=".45" stop-color="#b0308f"/><stop offset=".75" stop-color="#3a7bd0"/><stop offset="1" stop-color="#1a1530"/></linearGradient></defs>
    <path d="M0 22 C260 -60 500 120 512 477 L0 477 Z" fill="var(--orange)"/>
    <path d="M0 42 C250 -30 478 130 491 477 L0 477 Z" fill="url(#neon)" role="img" aria-label="Row of glowing neon display panels along a street at night"/>
  </svg>
  <p class="abs copy" style="left:563px;top:140px;width:507px">Lorem ipsum dolor sit amet, consectetur adipiscing elit, sed do eiusmod tempor incididunt ut labore et dolore magna aliqua. Ut enim ad minim veniam, quis nostrud exercitation ullamco laboris nisi ut aliquip ex ea commodo consequat. Duis aute irure dolor in reprehenderit in voluptate velit esse cillum dolore eu fugiat nulla pariatur.</p>
  <div class="abs h-sub" style="left:561px;top:300px">Vision
    <svg width="22" height="22" viewBox="0 0 22 22"><circle cx="11" cy="11" r="9" fill="none" stroke="var(--orange)" stroke-width="1.6"/><circle cx="11" cy="11" r="4.5" fill="none" stroke="var(--orange)" stroke-width="1.6"/><path d="M11 0v6M11 16v6M0 11h6M16 11h6" stroke="var(--orange)" stroke-width="1.6"/></svg></div>
  <p class="abs copy" style="left:563px;top:348px;width:507px">Lorem ipsum dolor sit amet, consectetur adipiscing elit, sed do eiusmod tempor incididunt ut labore et dolore magna aliqua. Ut enim</p>
  <div class="abs h-sub" style="left:561px;top:425px">Mission
    <svg width="26" height="26" viewBox="0 0 26 26"><path d="M13 3a10 10 0 1 0 10 10M13 8a5 5 0 1 0 5 5" fill="none" stroke="var(--orange)" stroke-width="1.8"/><path d="M13 13L23 3M19 3h4v4" fill="none" stroke="var(--orange)" stroke-width="1.8"/></svg></div>
  <p class="abs copy" style="left:563px;top:473px;width:507px">Lorem ipsum dolor sit amet, consectetur adipiscing elit, sed do eiusmod tempor incididunt ut labore et dolore magna aliqua. Ut enim</p>
  <p class="abs copy" style="left:563px;top:530px;width:507px">Lorem ipsum dolor sit amet, consectetur adipiscing elit, sed do eiusmod tempor incididunt ut labore et dolore magna aliqua. Ut enim</p>
</section>

<!-- Services -->
<section class="slide" style="top:1342px">
  <div class="abs services-top" role="img" aria-label="Orange-tinted backdrop of billboard posters"></div>
  <div class="brand light" style="left:50px;top:50px"><span class="brand-dot"></span><span class="brand-name">VULPO<small>DESIGN</small></span></div>
  <div class="abs white-band">OUR SERVICES</div>
  <p class="abs services-copy">Sed ut perspiciatis unde omnis iste natus error sit voluptatem accusantium doloremque laudantium, totam rem aperiam, eaque ipsa quae ab illo inventore veritatis et quasi architecto beatae vitae dicta sunt explicabo. Nemo enim ipsam voluptatem quia voluptas sit aspernatur</p>

  <div class="service" style="left:40px">
    <div class="service-ring"><div class="service-dot orange">
      <svg width="70" height="70" viewBox="0 0 70 70" fill="none" stroke="#fff" stroke-width="2.6" stroke-linejoin="round"><path d="M14 44l26-26 12 12-26 26z"/><path d="M14 44l-4 4 12 12 4-4"/><path d="M22 52l6 10"/><path d="M46 14l3-6M54 22l6-3M52 16l5-5"/></svg>
    </div></div>
    <h3>Lorem Ipsum</h3>
    <p>Sed ut perspiciatis unde omnis iste natus<br>error sit voluptatem accusantium<br>doloremque laudantium,</p>
  </div>
  <div class="service" style="left:291px">
    <div class="service-ring"><div class="service-dot black">
      <svg width="76" height="76" viewBox="0 0 76 76" fill="none" stroke="#fff" stroke-width="2.4"><rect x="8" y="28" width="26" height="22" rx="3"/><path d="M16 34l-2 12M24 34l-2 12M12 38h16M11 43h16"/><rect x="36" y="12" width="30" height="24" rx="3"/><path d="M44 30v-8h4l4-6v14z"/><rect x="28" y="48" width="24" height="18" rx="3"/><path d="M40 62l-6-6a3 3 0 0 1 6-3 3 3 0 0 1 6 3z"/></svg>
    </div></div>
    <h3>Lorem Ipsum</h3>
    <p>Sed ut perspiciatis unde omnis iste natus<br>error sit voluptatem accusantium<br>doloremque laudantium,</p>
  </div>
  <div class="service" style="left:545px">
    <div class="service-ring"><div class="service-dot orange">
      <svg width="76" height="76" viewBox="0 0 76 76" fill="none" stroke="#fff" stroke-width="2.4"><rect x="8" y="12" width="22" height="16" rx="2"/><path d="M16 16v8l7-4z"/><rect x="40" y="8" width="26" height="18" rx="2"/><path d="M45 14h16M45 20h12"/><path d="M10 46l22-8v26l-22-8z"/><path d="M32 44c6 2 6 12 0 14"/><path d="M50 56a4 4 0 0 1 7-3 4 4 0 0 1 7 3l-7 7z"/></svg>
    </div></div>
    <h3>Lorem Ipsum</h3>
    <p>Sed ut perspiciatis unde omnis iste natus<br>error sit voluptatem accusantium<br>doloremque laudantium,</p>
  </div>
  <div class="service" style="left:796px">
    <div class="service-ring"><div class="service-dot black">
      <svg width="70" height="70" viewBox="0 0 70 70" fill="none" stroke="#fff" stroke-width="2.2"><rect x="8" y="12" width="54" height="36" rx="2"/><path d="M28 48v8M42 48v8M20 58h30"/><rect x="32" y="20" width="24" height="16"/><path d="M14 20h12M14 26h12M14 32h12"/><path d="M37 31l3-7 3 7M47 24h4v7h-4"/></svg>
    </div></div>
    <h3>Lorem Ipsum</h3>
    <p>Sed ut perspiciatis unde omnis iste natus<br>error sit voluptatem accusantium<br>doloremque laudantium,</p>
  </div>
</section>

<!-- Projects -->
<section class="slide" style="top:1987px">
  <div class="brand" style="left:46px;top:35px"><span class="brand-dot"></span><span class="brand-name">VULPO<small>DESIGN</small></span></div>
  <div class="banner-right" style="left:545px;top:28px;width:551px;height:84px">PROJECTS</div>
  <div class="photo" style="left:52px;top:141px;width:240px;height:429px;background:linear-gradient(180deg,#c8ccd3,#6d7886 60%,#8a8f93)" role="img" aria-label="Street billboard showing a fashion sale poster"></div>
  <div class="photo" style="left:309px;top:141px;width:263px;height:429px;background:linear-gradient(180deg,#9aa3a8,#6b5640 45%,#b68c5d)" role="img" aria-label="Bus shelter billboard showing a travel poster"></div>
  <p class="abs copy" style="left:610px;top:137px;width:470px">Lorem ipsum dolor sit amet, consectetur adipiscing elit, sed do eiusmod tempor incididunt ut labore et dolore magna aliqua. Ut enim ad minim veniam, quis nostrud exercitation ullamco laboris nisi ut aliquip ex ea commodo consequat.</p>
  <div class="photo" style="left:609px;top:245px;width:464px;height:167px;background:linear-gradient(90deg,#3b3d42,#c96a2a 40%,#444650 60%,#d27a2e 85%,#3a3b40)" role="img" aria-label="Three backlit billboard mockups with portrait posters"></div>
  <div class="photo" style="left:607px;top:426px;width:466px;height:167px;background:linear-gradient(90deg,#8e96a3,#5b6f92 30%,#3a3d45 55%,#8a7168 80%,#9ba0a8)" role="img" aria-label="Three subway billboard mockups with fitness and fashion posters"></div>
</section>

<!-- Statistics -->
<section class="slide" style="top:2636px">
  <div class="abs" style="left:624px;top:0;width:472px;height:617px;background:linear-gradient(180deg,#6a6461,var(--panel))" role="img" aria-label="Dimmed backdrop of billboard posters"></div>
  <div class="brand" style="left:46px;top:35px"><span class="brand-dot"></span><span class="brand-name">VULPO<small>DESIGN</small></span></div>
  <div class="banner-left display" style="left:0;top:131px;width:511px;height:85px;font-size:42px;padding-left:58px;display:flex;align-items:center">OUR STATISTICS</div>
  <p class="abs" style="left:46px;top:240px;width:470px;font-size:14px;line-height:31.5px;color:var(--text)">Sed ut perspiciatis unde omnis iste natus error sit voluptatem accusantium doloremque laudantium, totam rem aperiam, eaque ipsa quae ab illo inventore veritatis et quasi architecto beatae vitae dicta sunt explicabo. Nemo enim ipsam voluptatem quia voluptas sit aspernatur</p>
  <div class="stat" style="left:679px;top:58px"><div class="stat-core orange">150+<br>Clients</div></div>
  <div class="stat" style="left:846px;top:188px"><div class="stat-core black">100+<br>Projects</div></div>
  <div class="stat" style="left:670px;top:291px"><div class="stat-core black">70+<br>Employers</div></div>
  <div class="stat" style="left:865px;top:388px"><div class="stat-core orange">25+<br>Years<br>Experience</div></div>
</section>

<!-- Team -->
<section class="slide" style="top:3283px">
  <div class="brand" style="left:46px;top:35px"><span class="brand-dot"></span><span class="brand-name">VULPO<small>DESIGN</small></span></div>
  <div class="banner-right" style="left:545px;top:28px;width:551px;height:84px">OUR TEAM</div>
  <div class="member" style="left:31px"><div class="portrait" role="img" aria-label="Portrait photo of team member"></div><h4>Marcus Hale</h4><p>Lorem ipsum dolor sit amet, consectetur adipiscing elit, sed do eiusmod tempor incididunt ut labore et dolore magna aliqua. Ut enim ad minim veniam, quis nostrud exercitation ullamco laboris nisi ut aliquip ex ea commodo consequat.</p></div>
  <div class="member" style="left:293px"><div class="portrait" role="img" aria-label="Portrait photo of team member"></div><h4>Nina Ortega</h4><p>Lorem ipsum dolor sit amet, consectetur adipiscing elit, sed do eiusmod tempor incididunt ut labore et dolore magna aliqua. Ut enim ad minim veniam, quis nostrud exercitation ullamco laboris nisi ut aliquip ex ea commodo consequat.</p></div>
  <div class="member" style="left:553px"><div class="portrait" role="img" aria-label="Portrait photo of team member"></div><h4>Owen Brask</h4><p>Lorem ipsum dolor sit amet, consectetur adipiscing elit, sed do eiusmod tempor incididunt ut labore et dolore magna aliqua. Ut enim ad minim veniam, quis nostrud exercitation ullamco laboris nisi ut aliquip ex ea commodo consequat.</p></div>
  <div class="member" style="left:815px"><div class="portrait" role="img" aria-label="Portrait photo of team member"></div><h4>Clara Venn</h4><p>Lorem ipsum dolor sit amet, consectetur adipiscing elit, sed do eiusmod tempor incididunt ut labore et dolore magna aliqua. Ut enim ad minim veniam, quis nostrud exercitation ullamco laboris nisi ut aliquip ex ea commodo consequat.</p></div>
</section>

</body>
</html>
```